Corrabeen Holiday Village Flyer Project

Flyer required for a holiday caravan park. I have attached the current flyer for the park and would like to use the same layout. Please also alter the changes to the text that I have marked up. Until the additional uploads for the new images are ready, could you please just leave those as a blank square and the images can be inserted once I have them loaded.

Target Market(s)

Holiday makers

Industry/Entity Type

Tourism

Colors
3176b5
33a6d7
0393ce
fbee3e
fbed22
ffffff
faa54b

Requirements
Must have
• copy the attached flyer
• Would like a better title font for the front text - "Corrabeen Holiday Village", please make that a more playful holiday feel font
• Please use images 001 & 002 as the front cover images
• I have more images to load up which will be done 4/7.
Nice to have
• would like a better colour back ground to the flyer, maybe blue-ish and then alter the colour of the text accordingly
Should not have
• Please use the attached flyer copy as a template

```html
<!DOCTYPE html>
<html lang="en">
<head>
<meta charset="utf-8">
<title>Corrabeen Holiday Village – Trifold Flyer</title>
<link rel="stylesheet" href="https://fonts.googleapis.com/css2?family=Fredoka:wght@600&family=Montserrat:ital,wght@0,500;0,600;0,700;0,800;1,600&display=swap">
<style>
:root{
  --stage:#5d6063;
  --navy:#1d3f73;
  --blue:#3176b5;
  --cyan:#33a6d7;
  --azure:#0393ce;
  --teal:#3ec2d0;
  --pale:#e4f3fa;
  --mist:#c9e6f3;
  --white:#ffffff;
}
*{box-sizing:border-box;margin:0;padding:0}
html,body{width:784px;height:1200px;overflow:hidden}
body{background:var(--stage);font-family:"Montserrat",sans-serif;color:var(--navy);position:relative}
.spread{position:absolute;left:20px;width:744px;height:548px;display:flex;background:var(--white);box-shadow:0 6px 18px rgba(0,0,0,.35)}
.spread--outside{top:28px}
.spread--inside{top:624px}
.panel{position:relative;width:248px;height:100%;overflow:hidden}
.panel + .panel{border-left:1px solid rgba(29,63,115,.12)}
.photo{position:absolute;display:block}

/* outside – left: location */
.panel--location{background:linear-gradient(180deg,#f3fafd 0%,var(--pale) 60%,var(--mist) 100%)}
.map{left:-60px;top:-70px;width:300px;height:300px;border-radius:50%;border:5px solid var(--blue);background:radial-gradient(circle at 40% 55%,#9fd36a 0%,#7cc357 35%,#44b7c6 60%,#2f9fd0 100%)}
.intro{position:absolute;left:18px;top:246px;width:214px;font-size:8.6px;font-weight:700;line-height:1.45;color:var(--blue);text-align:justify}
.band{background:var(--teal);color:var(--navy);font-weight:800;text-transform:uppercase}
.activities-head{position:absolute;left:0;top:330px;width:248px;padding:5px 16px;font-size:10px}
.activities{position:absolute;left:18px;top:358px;width:216px;display:flex;gap:10px;font-size:7.4px;font-weight:700;text-transform:uppercase;line-height:1.75}
.activities ul{list-style:none}
.activities ul:first-child{width:134px}
.activities ul + ul{border-left:1.5px solid var(--blue);padding-left:10px;white-space:nowrap}
.attractions{position:absolute;left:0;bottom:0;width:248px;padding:14px 16px 16px;font-size:12.5px;line-height:1.15;text-align:center}

/* outside – middle: back */
.panel--back{background:linear-gradient(180deg,#ffffff 0%,#eef8fc 45%,var(--mist) 100%)}
.wordmark{font-family:"Fredoka",sans-serif;font-weight:600;color:var(--blue);text-align:center;line-height:1}
.wordmark__name{display:block;font-size:34px;letter-spacing:1px}
.wordmark__sub{display:block;font-size:13px;letter-spacing:3px;margin-top:4px}
.panel--back .wordmark{position:absolute;left:0;right:0;top:150px}
.wave{position:absolute;left:0;width:100%}
.contact{position:absolute;left:22px;font-size:8.4px;font-weight:600;color:var(--navy);line-height:1.7}
.contact li{list-style:none;display:flex;align-items:center;gap:6px;white-space:nowrap}
.contact svg{width:10px;height:10px;flex:none}
.contact .web{margin-top:10px;font-size:10px;font-weight:700}
.panel--back .contact{top:312px}

/* outside – right: cover */
.panel--cover{background:linear-gradient(180deg,var(--blue) 0%,#4b8fcf 40%,#bfe2f2 70%,var(--pale) 100%)}
.panel--cover .wordmark{position:absolute;left:0;right:0;top:28px;color:var(--white)}
.cover-photo{left:0;top:100px;width:248px;height:220px;background:linear-gradient(180deg,#9ecbe8 0%,#6fb3dd 50%,#2a8cc4 100%)}
.cover-inset{left:112px;top:240px;width:124px;height:124px;border-radius:50%;border:4px solid var(--blue);background:linear-gradient(160deg,#a8d3ee 0%,#7a9db5 55%,#8b7a64 100%)}
.panel--cover .contact{top:400px}

/* inside – left: what to do */
.panel--todo{background:linear-gradient(180deg,#f3fafd 0%,var(--pale) 100%)}
.todo-head{position:absolute;left:0;top:24px;width:248px;padding:6px 18px;font-size:15px}
.todo{position:absolute;left:18px;top:66px;width:214px}
.todo section{margin-bottom:9px;padding-bottom:8px;border-bottom:1.5px solid var(--cyan)}
.todo section:last-child{border-bottom:0}
.todo h3{font-size:9.5px;font-style:italic;font-weight:600;color:var(--blue);margin-bottom:3px}
.todo .cols{display:flex;gap:16px;font-size:7.8px;font-weight:700;text-transform:uppercase;line-height:1.5}
.todo ul{list-style:none}
.todo-photo{left:0;top:312px;width:248px;height:236px;background:linear-gradient(180deg,#b8dcf0 0%,#8ab5cf 45%,#8c8168 100%)}

/* inside – middle */
.sea-photo{left:0;top:0;width:248px;height:548px;background:linear-gradient(180deg,#3b6f9c 0%,#1f7fbf 40%,#2c9bd4 75%,#6fc0e4 100%)}

/* inside – right: facilities */
.panel--facilities{background:linear-gradient(180deg,#ffffff 0%,var(--pale) 100%)}
.facilities-head{position:absolute;left:0;top:24px;width:248px;padding:6px 18px;font-size:14px}
.facilities{position:absolute;left:18px;top:62px;width:214px;display:flex;gap:12px;font-size:9.5px;font-weight:700;line-height:1.45}
.facilities ul{list-style:none}
.facilities ul + ul{border-left:2px solid var(--azure);padding-left:12px}
.nearby{position:absolute;left:18px;top:136px;width:214px;list-style:none;font-size:7.8px;font-weight:700;color:var(--blue);text-transform:uppercase;line-height:1.6}
.aerial{left:0;top:214px;width:248px;height:250px;background:linear-gradient(170deg,#2a8fc9 0%,#4aa8d8 40%,#8fb99a 70%,#c9b98f 100%)}
.more{position:absolute;left:18px;top:476px;width:214px;font-size:9px;font-weight:700;color:var(--blue);line-height:1.35}
.more .contact{position:static;margin-top:6px;font-size:7.8px;display:flex;gap:10px}
</style>
</head>
<body>

<svg width="0" height="0" style="position:absolute" aria-hidden="true">
  <defs>
    <symbol id="i-phone" viewBox="0 0 10 10"><circle cx="5" cy="5" r="5" fill="#3176b5"/><path d="M3.3 2.6l1 1-.5.6c.4.8.9 1.3 1.6 1.6l.6-.5 1 1-.7.8C4.6 7 3 5.4 2.6 3.3z" fill="#fff"/></symbol>
    <symbol id="i-pin" viewBox="0 0 10 10"><circle cx="5" cy="5" r="5" fill="#3176b5"/><path d="M5 2.2a1.8 1.8 0 0 1 1.8 1.8C6.8 5.3 5 7.8 5 7.8S3.2 5.3 3.2 4A1.8 1.8 0 0 1 5 2.2z" fill="#fff"/><circle cx="5" cy="4" r=".6" fill="#3176b5"/></symbol>
    <symbol id="i-mail" viewBox="0 0 10 10"><circle cx="5" cy="5" r="5" fill="#3176b5"/><rect x="2.5" y="3.2" width="5" height="3.6" fill="#fff"/><path d="M2.5 3.2L5 5.2l2.5-2" fill="none" stroke="#3176b5" stroke-width=".6"/></symbol>
    <symbol id="i-web" viewBox="0 0 10 10"><circle cx="5" cy="5" r="5" fill="#3176b5"/><circle cx="5" cy="5" r="2.6" fill="none" stroke="#fff" stroke-width=".7"/><path d="M2.4 5h5.2M5 2.4c-1.2 1.4-1.2 3.8 0 5.2M5 2.4c1.2 1.4 1.2 3.8 0 5.2" fill="none" stroke="#fff" stroke-width=".6"/></symbol>
  </defs>
</svg>

<!-- Outside of the trifold -->
<div class="spread spread--outside">

  <div class="panel panel--location">
    <div class="photo map" role="img" aria-label="Road map of the village location between Melrose Beach and the estuary, with routes to Mandurah and Bunbury"></div>
    <p class="intro">We are the second turn to left, after the bridge. Ideally located nestled between Melrose Beach and the Estuary, 3-minutes south of the Corrabeen cut with all the associated water activities and 15-minutes from Mandurah CBD boasting.</p>
    <h2 class="band activities-head">A range of activities such as</h2>
    <div class="activities">
      <ul>
        <li>Summer concerts</li>
        <li>Dolphin tours</li>
        <li>Movie theatres</li>
        <li>Superb restaurants</li>
        <li>Foreshore markets</li>
        <li>Seaview performing arts centre</li>
      </ul>
      <ul>
        <li>Wineries</li>
        <li>Wildlife parks</li>
        <li>Taverns</li>
        <li>Night clubs</li>
        <li>Festivals</li>
        <li>Art gallery</li>
      </ul>
    </div>
    <p class="band attractions">HISTORICAL SITES AND MANY MORE TOURIST ATTRACTIONS!</p>
  </div>

  <div class="panel panel--back">
    <h2 class="wordmark"><span class="wordmark__name">CORRABEEN</span><span class="wordmark__sub">HOLIDAY VILLAGE</span></h2>
    <svg class="wave" style="top:250px" height="60" viewBox="0 0 248 60" preserveAspectRatio="none" aria-hidden="true">
      <path d="M0 40 C60 10 140 10 248 30 L248 60 L0 60Z" fill="#c9e6f3"/>
      <path d="M0 40 C60 10 140 10 248 30" fill="none" stroke="#33a6d7" stroke-width="2"/>
    </svg>
    <ul class="contact">
      <li><svg><use href="#i-phone"/></svg>(08) 9500 2736</li>
      <li><svg><use href="#i-pin"/></svg>42 Shoreline Rd. Corrabeen 6210</li>
      <li><svg><use href="#i-mail"/></svg>info@corrabeenholiday.com.au</li>
      <li class="web"><svg><use href="#i-web"/></svg>www.corrabeenholiday.com.au</li>
    </ul>
  </div>

  <div class="panel panel--cover">
    <h1 class="wordmark"><span class="wordmark__name">CORRABEEN</span><span class="wordmark__sub">HOLIDAY VILLAGE</span></h1>
    <div class="photo cover-photo" role="img" aria-label="Children jumping from a jetty into the estuary on a sunny day"></div>
    <div class="photo cover-inset" role="img" aria-label="Family crabbing from a timber jetty"></div>
    <svg class="wave" style="top:330px" height="50" viewBox="0 0 248 50" preserveAspectRatio="none" aria-hidden="true">
      <path d="M0 20 C80 45 160 0 248 25" fill="none" stroke="#ffffff" stroke-width="2" opacity=".8"/>
    </svg>
    <ul class="contact">
      <li><svg><use href="#i-phone"/></svg>(08) 9500 2736</li>
      <li><svg><use href="#i-pin"/></svg>42 Shoreline Rd. Corrabeen 6210</li>
      <li><svg><use href="#i-mail"/></svg>info@corrabeenholiday.com.au</li>
      <li class="web"><svg><use href="#i-web"/></svg>www.corrabeenholiday.com.au</li>
    </ul>
  </div>
</div>

<!-- Inside of the trifold -->
<div class="spread spread--inside">

  <div class="panel panel--todo">
    <h2 class="band todo-head">What to do?</h2>
    <div class="todo">
      <section>
        <h3>The Estuary is only 2-minutes to the east for:</h3>
        <div class="cols">
          <ul><li>Water sports</li><li>Crabbing</li><li>Boat ramp access</li></ul>
          <ul><li>Swimming</li><li>Prawning</li><li>Boating</li></ul>
        </div>
      </section>
      <section>
        <h3>Melrose Beach is 5-minutes to the west for:</h3>
        <div class="cols">
          <ul><li>Water skiing</li><li>Swimming</li><li>Beach walking</li><li>Boat ramp access</li></ul>
          <ul><li>Crabbing</li><li>Sailing</li><li>Fishing</li><li>Surfing</li></ul>
        </div>
      </section>
      <section>
        <h3>Sporting Facilities 5-minutes</h3>
        <div class="cols"><ul><li>Golfing</li><li>Bowls</li></ul></div>
      </section>
    </div>
    <div class="photo todo-photo" role="img" aria-label="Grandfather and child crabbing from an old timber jetty"></div>
    <svg class="wave" style="top:296px" height="40" viewBox="0 0 248 40" preserveAspectRatio="none" aria-hidden="true">
      <path d="M0 0 L248 0 L248 16 C170 40 80 10 0 30Z" fill="#e4f3fa"/>
      <path d="M0 30 C80 10 170 40 248 16" fill="none" stroke="#3176b5" stroke-width="3"/>
    </svg>
  </div>

  <div class="panel panel--sea">
    <div class="photo sea-photo" role="img" aria-label="Dolphin leaping from the blue estuary water"></div>
  </div>

  <div class="panel panel--facilities">
    <h2 class="band facilities-head">Facilities</h2>
    <div class="facilities">
      <ul><li>EFTPOS</li><li>Swimming Pool</li><li>Undercover BBQ</li><li>Crab Cooker</li></ul>
      <ul><li>Playground</li><li>Laundrette</li><li>TV Room</li><li>Games Room</li></ul>
    </div>
    <ul class="nearby">
      <li>2 supermarkets within 2-minutes</li>
      <li>13 take-away shops within 7-minutes</li>
      <li>6 restaurants within 7-minutes</li>
      <li>Mandurah CBD 15-minutes</li>
    </ul>
    <div class="photo aerial" role="img" aria-label="Aerial view of the coastline, canal estates and the estuary channel"></div>
    <svg class="wave" style="top:200px" height="40" viewBox="0 0 248 40" preserveAspectRatio="none" aria-hidden="true">
      <path d="M0 0 L248 0 L248 10 C160 40 80 0 0 28Z" fill="#eaf6fb"/>
      <path d="M0 28 C80 0 160 40 248 10" fill="none" stroke="#33a6d7" stroke-width="3"/>
    </svg>
    <div class="more">
      <p>For more informations, please contact us or visit our website:</p>
      <ul class="contact">
        <li><svg><use href="#i-phone"/></svg>(08) 9500 2736</li>
        <li><svg><use href="#i-web"/></svg>www.corrabeenholiday.com.au</li>
      </ul>
    </div>
  </div>
</div>

</body>
</html>
```